General Dental Office Business Card

I run a private general dental office in southern California, and would like a refresh/redesign of my business card. I focus on quality care rather than volume. The email address on the uploaded current card should be updated to: info@maplecovedental.example. The current card's logo is a deboss, but I am open to other ideas. The logo can be refreshed, but it is something that's been with me since the beginning of the office, so I wouldn't want a drastic redesign.
Target Market(s)
Adults 18-99, whoever needs dental services
Industry/Entity Type
Healthcare/Dental
Contact Information for Business Card
Name, Address, Phone, email
Colors
Designer to choose colors to be used in the design.
Requirements
Must have
- Logo (Same as original one in the uploaded file), space on back for appointment time/date

```html
<!DOCTYPE html>
<html lang="en">
<head>
<meta charset="utf-8">
<title>Maple Cove Dental — Business Card</title>
<link href="https://fonts.googleapis.com/css2?family=Nunito+Sans:wght@400;600;700&display=swap" rel="stylesheet">
<style>
  :root {
    --backdrop: #3b3b3d;
    --teal: #2eb6c5;
    --teal-deep: #1e8e9b;
    --teal-text: #29afc0;
    --paper: #ffffff;
    --ink: #4a4a4a;
    --dots: #6b6b6b;
  }
  * { box-sizing: border-box; margin: 0; padding: 0; }
  html, body { width: 1200px; height: 689px; overflow: hidden; }
  body {
    background: var(--backdrop);
    font-family: "Nunito Sans", sans-serif;
    position: relative;
  }
  .card {
    position: absolute;
    top: 196px;
    width: 520px;
    height: 297px;
    background: var(--paper);
    overflow: hidden;
  }
  .card--back { left: 50px; }
  .card--front { left: 630px; }

  /* Practice name */
  .practice-name {
    font-weight: 600;
    line-height: 1.1;
    white-space: nowrap;
  }

  /* Back: appointment side */
  .back__band {
    position: absolute; left: 0; top: 0;
    width: 100%; height: 208px;
    background: var(--teal);
    display: flex; align-items: center; justify-content: center;
  }
  .practice-name--back {
    color: var(--teal-deep);
    font-size: 40px;
  }

  .appointment {
    position: absolute; left: 28px; right: 28px; bottom: 30px;
    display: flex; align-items: baseline;
    font-size: 14px; color: var(--ink);
  }
  .appointment__fill {
    flex: 1;
    border-bottom: 2px dotted var(--dots);
    margin: 0 6px;
    transform: translateY(-3px);
  }
  .appointment__fill--date { flex: 1.5; }

  /* Front: contact side */
  .practice-name--front {
    position: absolute; left: 34px; top: 134px;
    color: var(--teal-text);
    font-size: 23px;
  }

  .front__rule {
    position: absolute; left: 268px; top: 62px;
    width: 1.5px; height: 176px;
    background: var(--teal-text);
  }
  .contact {
    position: absolute; left: 284px; top: 58px;
    color: var(--ink); font-size: 12.5px; line-height: 1.35;
  }
  .contact__name { color: var(--teal-text); font-size: 18px; font-weight: 700; line-height: 1.2; }
  .contact__title { font-size: 13px; margin-bottom: 14px; }
  .contact__address { margin-bottom: 12px; }
  .contact__line { display: flex; align-items: center; gap: 6px; }
  .contact__icon { width: 11px; height: 11px; fill: var(--teal-text); flex: none; }
</style>
</head>
<body>
  <section class="card card--back" aria-label="Card back, appointment reminder">
    <div class="back__band">
      <div class="practice-name practice-name--back">Maple Cove Dental</div>
    </div>
    <div class="appointment">
      <span>Date:</span><span class="appointment__fill appointment__fill--date"></span>
      <span>Time:</span><span class="appointment__fill"></span>
      <span>Am/Pm</span>
    </div>
  </section>

  <section class="card card--front" aria-label="Card front, contact details">
    <div class="practice-name practice-name--front">Maple Cove Dental</div>
    <div class="front__rule"></div>
    <div class="contact">
      <div class="contact__name">Daniel R. Moreno DDS</div>
      <div class="contact__title">General Dentistry</div>
      <div class="contact__address">1820 Harbor View Road<br>Coastline, CA 92700</div>
      <div class="contact__line">
        <svg class="contact__icon" viewBox="0 0 24 24" aria-hidden="true"><path d="M6.6 10.8a15.1 15.1 0 0 0 6.6 6.6l2.2-2.2a1 1 0 0 1 1-.25 11.4 11.4 0 0 0 3.6.57 1 1 0 0 1 1 1V20a1 1 0 0 1-1 1A17 17 0 0 1 3 4a1 1 0 0 1 1-1h3.5a1 1 0 0 1 1 1c0 1.25.2 2.45.57 3.6a1 1 0 0 1-.25 1z"/></svg>
        <span>555-014-2828</span>
      </div>
      <div class="contact__line">
        <svg class="contact__icon" viewBox="0 0 24 24" aria-hidden="true"><path d="M2 5h20v2l-10 7L2 7z"/><path d="M2 8.5l10 7 10-7V19H2z"/></svg>
        <span>info@maplecovedental.example</span>
      </div>
      <div class="contact__line">
        <svg class="contact__icon" viewBox="0 0 24 24" aria-hidden="true"><path d="M12 2a10 10 0 1 0 0 20 10 10 0 0 0 0-20zm0 2c.9 0 2.3 2 2.8 7H9.2C9.7 6 11.1 4 12 4zM4.1 13h3.1c.1 2.2.5 4.1 1.1 5.5A8 8 0 0 1 4.1 13zm0-2a8 8 0 0 1 4.2-5.5C7.7 6.9 7.3 8.8 7.2 11zm7.9 9c-.9 0-2.3-2-2.8-7h5.6c-.5 5-1.9 7-2.8 7zm3.7-1.5c.6-1.4 1-3.3 1.1-5.5h3.1a8 8 0 0 1-4.2 5.5zM16.8 11c-.1-2.2-.5-4.1-1.1-5.5A8 8 0 0 1 19.9 11z"/></svg>
        <span>www.maplecovedental.example</span>
      </div>
    </div>
  </section>
</body>
</html>
```